K&R Security Services PTY. LTD.

Ive just had my logo made and I'm looking for some simple but strong designs for my business cards the company is a security company.

Please use dark colors.

Regards,

Owen Deloit

Reason: Need more time for discussion with other directors

Industry/Entity Type

Security

Font styles to use
Sans Serif
Decorative

```html
<!DOCTYPE html>
<html lang="en">
<head>
<meta charset="utf-8">
<title>K&amp;R Security Services – Business Card</title>
<link href="https://fonts.googleapis.com/css2?family=Jura:wght@500;600&display=swap" rel="stylesheet">
<style>
  :root {
    --backdrop: #5e5e5e;
    --card-dark: #2b2b2b;
    --card-light: #ffffff;
    --ink-light: #ffffff;
    --ink-dark: #2b2b2b;
    --mark-grey: #8a8a8a;
  }
  * { margin: 0; padding: 0; box-sizing: border-box; }
  html, body {
    width: 1200px; height: 1000px; overflow: hidden;
    background: var(--backdrop);
    font-family: "Jura", sans-serif;
  }
  .sheet {
    position: relative; width: 1200px; height: 1000px;
    display: flex; justify-content: center; align-items: center; gap: 60px;
  }
  .card {
    position: relative; width: 400px; height: 682px;
    background: var(--card-light);
    box-shadow: 0 6px 18px rgba(0,0,0,0.35);
    overflow: hidden;
  }
  /* Front */
  .front-top {
    position: absolute; left: 0; top: 0; width: 100%; height: 399px;
    background: var(--card-dark); color: var(--ink-light);
    text-align: center;
  }
  .holder-name {
    margin-top: 40px; font-size: 34px; font-weight: 600; letter-spacing: 1px;
  }
  .holder-role { font-size: 18px; font-weight: 500; margin-top: 2px; }
  .contact-list {
    position: absolute; top: 272px; left: 0; width: 100%;
    list-style: none; font-size: 19px; font-weight: 500; line-height: 23px;
    display: flex; flex-direction: column; align-items: center;
  }
  .contact-list li { display: flex; align-items: center; gap: 8px; }
  .contact-list svg { width: 13px; height: 15px; fill: none; stroke: var(--ink-light); stroke-width: 1.6; }
  .brand-mark {
    position: absolute; left: 0; width: 100%;
    display: flex; flex-direction: column; align-items: center; gap: 10px;
    color: var(--ink-dark); font-weight: 600;
  }
  .brand-mark .brand-square { background: var(--mark-grey); }
  .front-mark { top: 470px; font-size: 40px; }
  .front-mark .brand-square { width: 60px; height: 60px; }
  .front-mark .brand-sub { font-size: 40px; }
  /* Back */
  .back-mark { top: 190px; font-size: 64px; line-height: 1.05; }
  .back-mark .brand-square { width: 110px; height: 110px; margin-bottom: 10px; }
  .web-band {
    position: absolute; left: 0; top: 583px; width: 100%; height: 40px;
    background: var(--card-dark); color: var(--ink-light);
    font-size: 22px; font-weight: 500; text-align: center; line-height: 40px;
    letter-spacing: 0.5px;
  }
</style>
</head>
<body>
<main class="sheet">
  <section class="card card-front">
    <div class="front-top">
      <h1 class="holder-name">Owen Deloit</h1>
      <p class="holder-role">Owner</p>
      <ul class="contact-list">
        <li><svg viewBox="0 0 13 15"><rect x="3" y="1" width="7" height="13" rx="1"/><line x1="5" y1="11.5" x2="8" y2="11.5"/></svg>+00 410 555 010</li>
        <li><svg viewBox="0 0 13 15"><path d="M4 1 L2 3 Q2 10 9 13 L11 11 L9 9 L7.5 10 Q5 8.5 4.5 6 L6 5 Z"/></svg>+00 3 5550 1234</li>
        <li><svg viewBox="0 0 13 15"><rect x="1" y="3" width="11" height="9"/><polyline points="1,3 6.5,8 12,3"/></svg>owen@krsecurity.example</li>
      </ul>
    </div>
    <div class="brand-mark front-mark">
      <span class="brand-square"></span>
      <span class="brand-sub">K&amp;R Security</span>
    </div>
  </section>

  <section class="card card-back">
    <div class="brand-mark back-mark">
      <span class="brand-square"></span>
      <span>K&amp;R</span>
      <span>Security</span>
    </div>
    <div class="web-band">www.krsecurity.example</div>
  </section>
</main>
</body>
</html>
```